Essential Oil 15ml - package of 6

Design of a box of 6 different essential oils.
+ design of the bottle stickers
My bottles are 15ml clear blue glass.

The pictures attached are my competitors...

Target Market(s)

BRAMBLEWICK USA

Font styles to use
Serif

Requirements
Must have
• Our logo + "essential oil" and type (lavender, eucalyptus etc....)
• 15ml - 0.50 fl.oz.
• special color for the oil type.

```html
<!DOCTYPE html>
<html lang="en">
<head>
<meta charset="utf-8">
<title>Tel Amira Essential Oil Labels</title>
<link rel="stylesheet" href="https://fonts.googleapis.com/css2?family=Marcellus&family=Open+Sans:wght@300;400&display=swap">
<style>
  :root {
    --page: #ffffff;
    --label: #2c2c2e;
    --label-edge: #1f1f21;
    --ink-light: #f2f2f2;
    --ink-soft: #d8d8d8;
    --pill: #e9e9e9;
    --pill-ink: #2a2a2a;
    --pink: #d6529c;
    --orange: #e5762e;
    --green: #a9cf5f;
    --purple: #4e3a6e;
    --red: #e0232b;
  }
  * { box-sizing: border-box; margin: 0; padding: 0; }
  html, body {
    width: 1200px; height: 854px; overflow: hidden;
    background: var(--page);
  }
  .label-row {
    width: 1200px; height: 854px;
    display: flex; justify-content: center; align-items: center;
    gap: 28px;
  }
  .label {
    width: 202px; height: 330px;
    background: linear-gradient(90deg, var(--label-edge) 0%, var(--label) 18%, #363638 55%, var(--label) 85%, var(--label-edge) 100%);
    border-radius: 6px;
    display: flex; flex-direction: column; align-items: center;
    padding-top: 30px;
    color: var(--ink-light);
  }
  .brand-mark {
    width: 58px; height: 58px; border-radius: 50%;
    background: var(--ink-soft);
  }
  .brand-name {
    font-family: "Marcellus", serif;
    font-size: 31px; line-height: 1;
    margin-top: 14px;
    color: var(--ink-light);
  }
  .product-type {
    margin-top: 18px;
    width: 150px; height: 26px;
    border-radius: 13px;
    background: var(--pill);
    border: 2px solid #9a9a9a;
    color: var(--pill-ink);
    font-family: "Open Sans", sans-serif;
    font-size: 16px; line-height: 22px;
    text-align: center;
  }
  .claim {
    margin-top: 16px;
    font-family: "Open Sans", sans-serif;
    font-weight: 400;
    font-size: 15px;
    color: var(--ink-soft);
  }
  .oil-band {
    margin-top: 14px;
    width: 100%; height: 56px;
    display: flex; align-items: center; justify-content: center;
    font-family: "Open Sans", sans-serif;
    font-weight: 300;
    font-size: 26px; letter-spacing: 0.5px;
    color: var(--ink-light);
  }
  .oil-band--pink { background: linear-gradient(180deg, #c8458f, var(--pink)); }
  .oil-band--orange { background: linear-gradient(180deg, #d8681f, var(--orange)); }
  .oil-band--green { background: linear-gradient(180deg, #98c04d, var(--green)); }
  .oil-band--purple { background: linear-gradient(180deg, #44325f, var(--purple)); }
  .oil-band--red { background: linear-gradient(180deg, #cf1a22, var(--red)); }
  .volume {
    margin-top: 20px;
    font-family: "Open Sans", sans-serif;
    font-size: 9px;
    color: var(--ink-soft);
  }
</style>
</head>
<body>
<main class="label-row">
  <section class="label">
    <div class="brand-mark"></div>
    <h1 class="brand-name">Tel Amira</h1>
    <p class="product-type">Essential oil</p>
    <p class="claim">100% Natural</p>
    <p class="oil-band oil-band--pink">EUCALYPTUS</p>
    <p class="volume">15 ml ( 0.507 Oz )</p>
  </section>
  <section class="label">
    <div class="brand-mark"></div>
    <h1 class="brand-name">Tel Amira</h1>
    <p class="product-type">Essential oil</p>
    <p class="claim">100% Natural</p>
    <p class="oil-band oil-band--orange">EUCALYPTUS</p>
    <p class="volume">15 ml ( 0.507 Oz )</p>
  </section>
  <section class="label">
    <div class="brand-mark"></div>
    <h1 class="brand-name">Tel Amira</h1>
    <p class="product-type">Essential oil</p>
    <p class="claim">100% Natural</p>
    <p class="oil-band oil-band--green">EUCALYPTUS</p>
    <p class="volume">15 ml ( 0.507 Oz )</p>
  </section>
  <section class="label">
    <div class="brand-mark"></div>
    <h1 class="brand-name">Tel Amira</h1>
    <p class="product-type">Essential oil</p>
    <p class="claim">100% Natural</p>
    <p class="oil-band oil-band--purple">LAVENDER</p>
    <p class="volume">15 ml ( 0.507 Oz )</p>
  </section>
  <section class="label">
    <div class="brand-mark"></div>
    <h1 class="brand-name">Tel Amira</h1>
    <p class="product-type">Essential oil</p>
    <p class="claim">100% Natural</p>
    <p class="oil-band oil-band--red">EUCALYPTUS</p>
    <p class="volume">15 ml ( 0.507 Oz )</p>
  </section>
</main>
</body>
</html>
```